Brochure Design Project

hi
Im looking for a great little design for my brochures. I have a home beauty salon and need a brochure menu. The name of the business is Kanade SoftGlow which is a japanese name. I'm not japanese but want it to have a slight feel of japanese, perhaps some watercolour or a traditional pattern.
Salon menu will have waxing, Facials, massage etc and would like a tri fold brochure
No bright colours please or butterflies. I want it to look and feel relaxing and peaceful. Help with a nice Logo would also be great
thanks for your help
Updates

Project Deadline Extended
Reason: I know a lot of you are busy but by extending the timeframe I can hopefully get all your creative minds flowing

hi

Just thought I'd add that I would like the brochures to be modern and edgy looking
thanks so far

Target Market(s)

People that want to be pampered and look and feel great and have a sort of natural feel ( if that makes sense)

Industry/Entity Type

Beauty Salon

Requirements
Must have
• I would like it to be A4 size and folded as a tri brochure,
Nice to have
• A classy font
Should not have
• Butterflies, swirls, bright colours or purple

```html
<!DOCTYPE html>
<html lang="en">
<head>
<meta charset="utf-8">
<title>Kanade SoftGlow – Tri-fold Brochure</title>
<link href="https://fonts.googleapis.com/css2?family=Didact+Gothic&display=swap" rel="stylesheet">
<style>
  :root {
    --sky: #a7cbee;
    --sky-pale: #c6e6f3;
    --blush: #f6d2e1;
    --blush-deep: #f3c3d6;
    --rose: #d9659f;
    --rose-soft: #e58cb9;
    --ink: #4b4b52;
    --ink-soft: #5e5e66;
    --card: #fdeef5;
    --lilac-bubble: rgba(186, 184, 222, 0.45);
    --pink-bubble: rgba(240, 170, 200, 0.45);
    --fold: rgba(255, 255, 255, 0.55);
  }
  * { box-sizing: border-box; margin: 0; padding: 0; }
  html, body {
    width: 1200px; height: 937px; overflow: hidden;
    background: #ffffff;
    font-family: "Didact Gothic", "Century Gothic", sans-serif;
    color: var(--ink);
  }
  .brochure {
    position: relative;
    width: 1200px; height: 937px;
    display: flex;
    background: linear-gradient(180deg, var(--sky) 0%, #cfd5ee 45%, var(--blush) 80%, var(--blush-deep) 100%);
  }
  .panel {
    position: relative;
    width: 400px; height: 937px;
    overflow: hidden;
  }
  .panel + .panel { border-left: 1px solid var(--fold); }
  .panel--front {
    background: linear-gradient(180deg, var(--sky-pale) 0%, #d4e7f2 40%, #f0d6e6 75%, var(--blush) 100%);
  }
  .bubbles { position: absolute; left: 0; top: 0; width: 400px; height: 937px; pointer-events: none; }

  /* Inside fold */
  .blossom-branch {
    position: absolute; left: 0; top: 0; width: 440px; height: 180px;
    background: radial-gradient(ellipse at 30% 55%, rgba(248, 200, 222, 0.9) 0%, rgba(248, 200, 222, 0.5) 35%, rgba(248, 200, 222, 0) 70%);
  }
  .feature { position: absolute; left: 40px; width: 322px; }
  .feature__title {
    font-size: 27px; font-weight: 400; letter-spacing: 0.5px;
    color: var(--ink); text-transform: uppercase; line-height: 1;
    margin-bottom: 6px;
  }
  .feature__body { font-size: 16px; line-height: 23px; color: var(--ink-soft); }
  .feature--one { top: 198px; }
  .feature--two { top: 420px; }
  .feature--three { top: 641px; }

  /* Back */
  .services {
    position: absolute; left: 84px; top: 71px; width: 230px; height: 586px;
    background: var(--card);
    text-align: center;
    padding-top: 16px;
  }
  .services__heading {
    font-size: 26px; color: var(--rose-soft); letter-spacing: 1px;
    margin-bottom: 10px;
  }
  .service { margin-bottom: 8px; }
  .service__name { font-size: 19px; line-height: 22px; color: var(--ink); text-transform: uppercase; }
  .service__desc { font-size: 13.5px; line-height: 18px; color: var(--ink-soft); font-style: italic; }
  .booking {
    position: absolute; left: 0; width: 400px; top: 850px; text-align: center;
  }
  .booking__label { font-size: 17px; color: var(--ink); }
  .booking__phone { font-size: 26px; color: var(--rose-soft); letter-spacing: 1px; margin-top: 2px; }

  /* Front */
  .hero { position: absolute; left: 0; top: 0; width: 400px; height: 400px; }
  .brand {
    position: absolute; left: 0; width: 400px; top: 410px; text-align: center;
  }
  .brand__name { font-size: 96px; line-height: 1; color: var(--rose); letter-spacing: 1px; }
  .brand__tagline { font-size: 34px; color: var(--ink); letter-spacing: 3px; margin-top: 6px; }
  .contact {
    position: absolute; left: 0; width: 400px; top: 857px; text-align: center;
    font-size: 18px; line-height: 25px; color: var(--ink);
  }
  .contact__dot { color: var(--rose-soft); }
</style>
</head>
<body>
<main class="brochure">

  <section class="panel panel--inside">
    <div class="blossom-branch" role="img" aria-label="Cherry blossom branch illustration"></div>
    <svg class="bubbles" viewBox="0 0 400 937" aria-hidden="true">
      <circle cx="190" cy="820" r="115" fill="none" stroke="rgba(255,255,255,0.4)" stroke-width="10"/>
      <circle cx="145" cy="995" r="95" fill="var(--pink-bubble)"/>
      <circle cx="260" cy="925" r="75" fill="var(--lilac-bubble)"/>
      <circle cx="320" cy="995" r="78" fill="var(--pink-bubble)"/>
    </svg>
    <article class="feature feature--one">
      <h2 class="feature__title">Title goes here</h2>
      <p class="feature__body">Tatus nidae. Evellis simaxim olent. Imusit ad es iur aboria denient aut quamusdam il morpo resenique que peris inulparum fuga. Et porem archicim reseque aspelidut fugitae volupisi.</p>
    </article>
    <article class="feature feature--two">
      <h2 class="feature__title">Title goes here</h2>
      <p class="feature__body">Tatus nidae. Evellis simaxim olent. Imusit ad es tio ssinis aspelidut fugitae volupisi quo vel lab resenique que peris inulparum fuga. Et porem archicim reseque aboria denient.</p>
    </article>
    <article class="feature feature--three">
      <h2 class="feature__title">Title goes here</h2>
      <p class="feature__body">Tatus nidae. Evellis simaxim olent. Imusit ad es tio ssinis aspelidut fugitae volupisi quo vel lab resenique que peris inulparum fuga. Et porem archicim reseque aboria denient.</p>
    </article>
  </section>

  <section class="panel panel--back">
    <svg class="bubbles" viewBox="0 0 400 937" aria-hidden="true">
      <circle cx="208" cy="772" r="85" fill="var(--lilac-bubble)"/>
      <circle cx="281" cy="836" r="60" fill="var(--pink-bubble)"/>
    </svg>
    <div class="services">
      <h2 class="services__heading">SERVICES:</h2>
      <div class="service"><p class="service__name">Facial treatment 1</p><p class="service__desc">Description if necessary</p></div>
      <div class="service"><p class="service__name">Facial treatment 2</p><p class="service__desc">Description if necessary</p></div>
      <div class="service"><p class="service__name">Massage</p><p class="service__desc">Description if necessary</p></div>
      <div class="service"><p class="service__name">Other treatment 1</p><p class="service__desc">Description if necessary</p></div>
      <div class="service"><p class="service__name">Other treatment 2</p><p class="service__desc">Description if necessary</p></div>
      <div class="service"><p class="service__name">Hair treatment 1</p><p class="service__desc">Description if necessary</p></div>
      <div class="service"><p class="service__name">Hair treatment 2</p><p class="service__desc">Description if necessary</p></div>
      <div class="service"><p class="service__name">Manicure</p><p class="service__desc">Description if necessary</p></div>
      <div class="service"><p class="service__name">Pedicure</p><p class="service__desc">Description if necessary</p></div>
      <div class="service"><p class="service__name">Waxing</p><p class="service__desc">Description if necessary</p></div>
    </div>
    <div class="booking">
      <p class="booking__label">Call to make an appointment:</p>
      <p class="booking__phone">(012) 555 0148</p>
    </div>
  </section>

  <section class="panel panel--front">
    <svg class="bubbles" viewBox="0 0 400 937" aria-hidden="true">
      <circle cx="200" cy="590" r="115" fill="none" stroke="rgba(255,255,255,0.45)" stroke-width="10"/>
      <circle cx="140" cy="735" r="90" fill="var(--pink-bubble)"/>
      <circle cx="255" cy="690" r="73" fill="var(--lilac-bubble)"/>
      <circle cx="320" cy="725" r="63" fill="var(--pink-bubble)"/>
    </svg>
    <svg class="hero" viewBox="0 0 400 400" aria-hidden="false">
      <defs>
        <linearGradient id="photoTone" x1="0" y1="0" x2="1" y2="1">
          <stop offset="0" stop-color="#e9c7b3"/>
          <stop offset="0.55" stop-color="#d9ab92"/>
          <stop offset="1" stop-color="#c9d9e4"/>
        </linearGradient>
      </defs>
      <path d="M2 215 C 20 80, 180 10, 400 5 L 400 16 C 200 24, 50 90, 12 215 Z" fill="#86b3e3"/>
      <path d="M20 210 C 40 110, 180 26, 400 20 L 400 270 C 300 330, 130 350, 50 310 C 22 295, 14 250, 20 210 Z"
            fill="url(#photoTone)" role="img" aria-label="Photo of a woman relaxing during a back massage"/>
      <path d="M10 250 C 8 330, 120 350, 220 335 C 300 323, 360 300, 400 280 L 400 290 C 340 325, 250 348, 180 352 C 80 358, 2 330, 10 250 Z" fill="#e98dbd"/>
      <circle cx="315" cy="290" r="62" fill="#f7c6dc" role="img" aria-label="Cherry blossom flower illustration"/>
    </svg>
    <div class="brand">
      <h1 class="brand__name">Kanade</h1>
      <p class="brand__tagline">SOFT GLOW</p>
    </div>
    <address class="contact" style="font-style: normal;">
      <p>Address information goes here</p>
      <p>Telephone no. <span class="contact__dot">•</span> Email or other info</p>
    </address>
  </section>

</main>
</body>
</html>
```